Label Sticker Design for Apothecary Brand

Hello! We are an independent grassroots business located in Ontario, Canada that specializes in making organic botanical and herbal skin care, tea, witchcraft and wellness products. We have been in business for 5 years and are looking to create a label sticker with one of our slogans for use in packaging.

Our brand is dark, herbal, witchy, and modern with old-world apothecary and vintage influences. We want a label that will be VERY clean, and easily explain what our product is, while conveying a sense of mysticism and magic, as well as a traditional apothecary vibe.

We have attached design inspiration to give you an idea of the style that we would like. Our demographic is hipster, current, (think finger tattoos, linen dresses, and organic groceries), and they care deeply about where we source our ingredients, and how we craft our product. We don't want an old-school sticker that looks like it should be on the shelves of a health food store. The design should be contemporary, upmarket, modern and clean, but evoke a strong sense of magic and self-care with wild gathered herbs and unusual wild flowers!

This will be used as a packaging sticker for our shipping boxes.

We look forward to your winning design!
Thank you very much.

Target Market(s)

20 - 50yr Female Demographic
Natural, bohemian, earthy, hipster and modern

Key Words: Minimalist Tattoos, Organic Skin Care, Bohemian, Witchy, Dark, Moody, Confident, Sustainable, Ethical,

PLEASE VIEW PHOTOS BEFORE SUBMITTING A DESIGN ;)

Industry/Entity Type

Skin Care Product

Font styles to use
Serif
Script

Colors
1b1b1b
5c5c5c
fbfbfb

Requirements
Must have
• Clean and Simple - Take a look at the photos we've posted!
• Black / greyscale (No color)
• Label sticker must be a rectangle (3" x 2")
• Very Modern with a touch of old-world
• We are open to a variety of font styles. Please see photo FONT in image files, or the images 'Bottle Inspiration'
• Please use the following text:
• Thornmoor Stillhouse
• --------------------
• Steeped by Moonlight
• * Once your design is chosen and purchased, we will require the names of all fonts and sources of imagery used.
Nice to have
• A moody botanical graphic surrounding the text. Tangled wild, antique botanical illustrations. Not mandatory, but would be very nice.
Should not have
• Colour
• Messy or overly dramatic fonts
• Cartoon Imagery
• Leaf Motif
• Female Body Silhouettes
• Scroll or decorative borders.
• Butterflies, birds etc
• Actual pictures of witches
• Mandalas or Messy Graphics

```html
<!DOCTYPE html>
<html lang="en">
<head>
<meta charset="utf-8">
<title>Thornmoor Stillhouse – Label</title>
<link rel="stylesheet" href="https://fonts.googleapis.com/css2?family=Old+Standard+TT&family=IM+Fell+English&display=swap">
<style>
  :root {
    --ink: #1b1b1b;
    --ink-soft: #5c5c5c;
    --paper: #fbfbfb;
  }
  html, body {
    margin: 0;
    padding: 0;
    width: 1200px;
    height: 425px;
    overflow: hidden;
    background: var(--paper);
  }
  .label {
    position: relative;
    width: 1200px;
    height: 425px;
    background: var(--paper);
    color: var(--ink);
  }
  .botanical-texture {
    position: absolute;
    inset: 0;
    background:
      radial-gradient(ellipse at 28% 30%, rgba(205,205,205,0.45), rgba(251,251,251,0) 45%),
      radial-gradient(ellipse at 78% 22%, rgba(195,195,195,0.5), rgba(251,251,251,0) 40%),
      radial-gradient(ellipse at 55% 80%, rgba(215,215,215,0.35), rgba(251,251,251,0) 45%),
      radial-gradient(ellipse at 5% 55%, rgba(220,220,220,0.35), rgba(251,251,251,0) 30%);
  }
  .frame {
    position: absolute;
    inset: 0;
  }
  .brand-name {
    position: absolute;
    left: 0;
    right: 0;
    top: 84px;
    margin: 0;
    text-align: center;
    font-family: "Old Standard TT", serif;
    font-weight: 400;
    font-size: 56px;
    letter-spacing: 1px;
    line-height: 64px;
    color: var(--ink);
  }
  .slogan {
    position: absolute;
    left: 0;
    right: 0;
    top: 178px;
    margin: 0;
    text-align: center;
    font-family: "Old Standard TT", serif;
    font-size: 28px;
    line-height: 34px;
    color: var(--ink);
  }
  .info {
    position: absolute;
    top: 296px;
    width: 270px;
    font-family: "IM Fell English", serif;
    color: var(--ink-soft);
  }
  .info h2 {
    margin: 0;
    font-family: "IM Fell English", serif;
    font-weight: 400;
    font-size: 19px;
    line-height: 19px;
    color: var(--ink);
  }
  .info p {
    margin: 0;
    font-size: 12.5px;
    line-height: 12.5px;
  }
  .info--ingredients { left: 21px; text-align: left; }
  .info--description { right: 20px; text-align: right; }
  .volume {
    position: absolute;
    left: 0;
    right: 0;
    top: 340px;
    margin: 0;
    text-align: center;
    font-family: "Old Standard TT", serif;
    font-size: 28px;
    line-height: 34px;
    color: var(--ink);
  }
</style>
</head>
<body>
<div class="label">
  <div class="botanical-texture" role="img" aria-label="Faint grey tangle of wild gathered herbs and branches behind the label text"></div>

  <svg class="frame" width="1200" height="425" viewBox="0 0 1200 425" aria-hidden="true">
    <g stroke="var(--ink)" stroke-width="2" fill="none">
      <line x1="44" y1="11" x2="1156" y2="11"/>
      <line x1="11" y1="415" x2="1156" y2="415"/>
      <line x1="11" y1="44" x2="11" y2="393"/>
      <line x1="1188" y1="44" x2="1188" y2="240"/>
      <line x1="300" y1="168" x2="900" y2="168" stroke-width="1.5"/>
    </g>
  </svg>

  <h1 class="brand-name">Thornmoor Stillhouse</h1>
  <p class="slogan">Steeped by Moonlight</p>

  <section class="info info--ingredients">
    <h2>List of ingredients:</h2>
    <p>Our brand is dark, herbal, witchy,<br>and modern with old-world apothecary<br>and vintage influences. We specialize in<br>making organic botanical and herbal<br>skin care, tea, witchcraft and wellness<br>Products.</p>
  </section>

  <p class="volume">50ml</p>

  <section class="info info--description">
    <h2>Description:</h2>
    <p>Our brand is dark, herbal, witchy,<br>and modern with old-world apothecary<br>and vintage influences. We specialize in<br>making organic botanical and herbal<br>skin care, tea, witchcraft and wellness<br>products.</p>
  </section>
</div>
</body>
</html>
```